Brightway Tidy Services strata flyer

Looking for a flyer that will grab peoples attention also need to include some kind off promotional offer on there so they will hold onto the flyer . Would like approximateley 4 pictures of appartment blocks. Would like to include the following services. Building management Common area cleaning ,window cleaning, lawn mowing, gardening , pressure cleaning, carpet cleaning, bin cleaning. Handy man services.

Target Market(s)

appartment blocks/strata managers

Industry/Entity Type

Pressure Cleaning

Font styles to use
Serif

Colors
0355a3
ceddec
ec2027

Requirements
Must have
• company logo & colors contact details email: Info@brightwaytidyservices.example.au
• Phone: 0498305127 website brightwaytidyservices.example.au

```html
<!DOCTYPE html>
<html lang="en">
<head>
<meta charset="utf-8">
<title>Brightway Tidy Services – Strata Flyer</title>
<link rel="stylesheet" href="https://fonts.googleapis.com/css2?family=Open+Sans:wght@400;600;700;800&display=swap">
<style>
  :root {
    --blue: #0355a3;
    --blue-light: #3d86d1;
    --pale: #ceddec;
    --pale-soft: #e3ecf6;
    --red: #ec2027;
    --white: #ffffff;
    --stage: #e8ebef;
  }
  * { box-sizing: border-box; margin: 0; padding: 0; }
  html, body { width: 1200px; height: 873px; overflow: hidden; }
  body {
    background: var(--stage);
    font-family: "Open Sans", Arial, sans-serif;
    position: relative;
  }
  .flyer {
    position: absolute;
    left: 400px; top: 16px;
    width: 400px; height: 840px;
    background: var(--white);
    overflow: hidden;
    box-shadow: 0 6px 18px rgba(0,0,0,.18);
  }
  .flyer-art { position: absolute; left: 0; top: 0; }
  .brand {
    position: absolute; left: 22px; top: 26px;
    display: flex; align-items: center; gap: 10px;
  }
  .brand-dot {
    width: 38px; height: 38px; border-radius: 50%;
    background: var(--blue);
  }
  .brand-name {
    color: var(--blue); font-weight: 800; font-size: 18px; line-height: 1.1;
    width: 150px;
  }
  .ribbon {
    position: absolute; right: 16px; top: 12px;
    background: var(--red); color: var(--white);
    font-weight: 800; font-size: 13px; letter-spacing: .3px;
    padding: 5px 14px 5px 20px;
    clip-path: polygon(0 0, 100% 0, 100% 100%, 0 100%, 8px 50%);
  }
  .services-title {
    position: absolute; left: 22px; top: 418px;
    color: var(--blue); font-weight: 800; font-size: 22px; line-height: 1.08;
    text-transform: uppercase;
  }
  .service-list {
    position: absolute; list-style: none;
    color: #222; font-size: 14.5px; line-height: 1.45;
  }
  .service-list.col-a { left: 22px; top: 476px; }
  .service-list.col-b { left: 240px; top: 416px; }
  .service-list li { display: flex; align-items: center; gap: 7px; }
  .service-list li::before {
    content: "›"; flex: none;
    width: 12px; height: 12px; border-radius: 50%;
    background: var(--red); color: var(--white);
    font-size: 11px; font-weight: 800; line-height: 10px; text-align: center;
  }
  .contact {
    position: absolute; left: 0; top: 648px; width: 400px;
    text-align: center;
  }
  .contact-cta {
    color: var(--red); font-weight: 800; font-size: 15px; text-transform: uppercase;
  }
  .contact-box {
    margin: 8px auto 0; width: 330px;
    border: 1px dashed #9fb7d3;
    padding: 6px 10px 8px;
  }
  .contact-phone {
    display: flex; align-items: center; justify-content: center; gap: 12px;
    color: var(--red); font-weight: 700; font-size: 34px; line-height: 1.1;
  }
  .contact-email {
    color: var(--blue); font-size: 14px; margin-top: 6px;
  }
  .web-band {
    position: absolute; left: 0; bottom: 0; width: 400px; height: 56px;
    background: var(--blue); color: var(--white);
    display: flex; align-items: center; justify-content: center;
    font-size: 19px; font-weight: 600;
  }
</style>
</head>
<body>
  <div class="flyer">
    <svg class="flyer-art" width="400" height="840" viewBox="0 0 400 840">
      <defs>
        <linearGradient id="tileA" x1="0" y1="0" x2="1" y2="1"><stop offset="0" stop-color="#b9c9d8"/><stop offset="1" stop-color="#e9ece8"/></linearGradient>
        <linearGradient id="tileB" x1="0" y1="0" x2="1" y2="1"><stop offset="0" stop-color="#6c7a85"/><stop offset="1" stop-color="#d8dde0"/></linearGradient>
        <linearGradient id="tileC" x1="0" y1="0" x2="1" y2="1"><stop offset="0" stop-color="#7fa6c9"/><stop offset="1" stop-color="#e4e8ea"/></linearGradient>
        <linearGradient id="tileD" x1="0" y1="0" x2="1" y2="1"><stop offset="0" stop-color="#8a9a6d"/><stop offset="1" stop-color="#c9a58e"/></linearGradient>
      </defs>
      <g class="photo-collage">
        <polygon role="img" aria-label="Photo of a modern apartment block with balconies" fill="url(#tileA)" points="190,40 400,40 400,205 230,205"/>
        <polygon role="img" aria-label="Photo of a grey apartment tower facade" fill="url(#tileB)" points="0,150 218,150 250,300 0,300"/>
        <polygon role="img" aria-label="Photo of apartment blocks under blue sky" fill="url(#tileC)" points="240,213 400,213 400,330 268,330"/>
        <polygon role="img" aria-label="Photo of a brick apartment building with trees" fill="url(#tileD)" points="0,308 252,308 276,400 0,400"/>
      </g>
      <path class="header-white" d="M0 0 H300 C250 50 190 120 0 178 Z" fill="var(--white)"/>
      <path d="M0 186 C170 140 230 70 330 0" fill="none" stroke="var(--blue)" stroke-width="10"/>
      <path d="M0 198 C180 150 250 80 360 0" fill="none" stroke="var(--blue-light)" stroke-width="4"/>
      <path d="M0 400 H400 V330 H276 Z" fill="var(--white)"/>
      <path class="contact-panel" d="M0 632 C130 632 270 600 400 540 V840 H0 Z" fill="var(--pale-soft)"/>
      <path d="M0 626 C130 626 270 594 400 532" fill="none" stroke="var(--blue)" stroke-width="9"/>
      <path d="M0 614 C140 614 270 584 400 520" fill="none" stroke="var(--blue-light)" stroke-width="3"/>
    </svg>

    <div class="brand">
      <span class="brand-dot"></span>
      <span class="brand-name">Brightway Tidy Services</span>
    </div>
    <div class="ribbon">FREE QUOTES!</div>

    <h2 class="services-title">Our Cleaning<br>Services Include:</h2>
    <ul class="service-list col-a">
      <li>Building Management</li>
      <li>Common Area Cleaning</li>
      <li>Window Cleaning</li>
      <li>Lawn Mowing</li>
      <li>Gardening</li>
    </ul>
    <ul class="service-list col-b">
      <li>Pressure Cleaning</li>
      <li>Carpet Cleaning</li>
      <li>Bin Cleaning</li>
      <li>Handy Man Services</li>
    </ul>

    <div class="contact">
      <p class="contact-cta">Call us now for free initial clean</p>
      <div class="contact-box">
        <p class="contact-phone">
          <svg width="44" height="36" viewBox="0 0 44 36" aria-hidden="true">
            <path d="M4 12 C4 4 40 4 40 12 L40 16 L30 16 L30 11 L14 11 L14 16 L4 16 Z" fill="var(--red)"/>
            <path d="M12 18 L32 18 L38 34 L6 34 Z" fill="var(--red)"/>
            <circle cx="22" cy="26" r="5" fill="var(--white)"/>
          </svg>
          049 830 5127
        </p>
        <p class="contact-email">Info@brightwaytidyservices.example.au</p>
      </div>
    </div>

    <div class="web-band">www.brightwaytidyservices.example.au</div>
  </div>
</body>
</html>
```